VelmaraStitch.com will be an online bespoke garment creator, specifically around designing your own Wedding Dress. It will enable you to specify your own material, colours and patterns and customized features such as bows, sequins, diamantes, and more from a selection of per-defined base garments and customize them to your taste.
The concept is similar to:
www.theorvandlane.example
But the design should reflect more like
www.quillbarn.example
www.dunwel.example - (in particular the build elements)
www.tarvo.example
It will be aimed at the Female marketplace. However this does not mean to use pink or portray the brand in very girly way. It should use good white space, and look very classy. not too busy, but functional and elegant, with a focus on stable and responsible site that will deliver. A wedding dress is an important purchase and to trust a company to make one for you from a distance takes a lot of trust from the customer perspective.
We want to first create the homepage and "build the dress" pages, which will consist of Enter your Measurements, Choose a Base Silhouette Style, Choose Fabric, Choose Colors, Customize Dress, Summary, Order Page, Thank you Page.
It will then have generic About us, How to Measure, Agent Locator, How it works, Contact, Order Samples, Support.
A very basic wire frame was created here to aid development, but the branding is being developed, so do not use any of it for inspiration just a visual interpretation - http://pexlarnode.example/velmara/
The link above is merely an idea on what areas the site will have. The actual design and colour scheme should reflect these sites.
The branding is also here - www.velmarastitch.example not the one used within that link.
The site will enable you to log in, save your designs and your delivery and measurement information. It will also offer the usual social media buttons to share the design and ability to leave comments.
This will be the first draft and the winning design will get to design the other pages and future work associated to the site.
thanks!

```html
<!DOCTYPE html>
<html lang="en">
<head>
<meta charset="utf-8">
<title>VelmaraStitch.com – Design Your Own Wedding Dress</title>
<link rel="stylesheet" href="https://fonts.googleapis.com/css2?family=Arimo:wght@400;700&family=Gelasio:wght@400;700&family=Ubuntu:wght@400;500;700&display=swap">
<style>
:root{
  --page-bg:#ebebeb;
  --header-bg:#e3e3e3;
  --ink:#1c1c1c;
  --text:#333333;
  --muted:#5a5a5a;
  --accent:#8c6a47;
  --rule:#d6d6d6;
  --footer-bg:#323436;
  --footer-head:#ffffff;
  --footer-link:#9b7b5a;
  --footer-note:#b4b4b4;
  --arrow:#5b5b5b;
}
*{box-sizing:border-box;margin:0;padding:0}
html,body{width:1200px;height:1185px;overflow:hidden}
body{background:var(--page-bg);font-family:"Arimo",Arial,sans-serif;color:var(--text);position:relative}
.abs{position:absolute}

/* header & hero */
.header-band{left:0;top:0;width:1200px;height:93px;background:var(--header-bg)}
.header-photo{left:0;top:0;width:760px;height:270px;
  background:
    radial-gradient(ellipse 120px 90px at 70px 40px,#f6f1de 0%,#efe8d2 45%,rgba(239,232,210,0) 100%),
    radial-gradient(ellipse 110px 40px at 190px 235px,#e3c9bf 0%,#e8d8d0 45%,rgba(235,225,220,0) 100%),
    radial-gradient(ellipse 90px 60px at 30px 150px,#e6d9b8 0%,rgba(230,220,190,0) 100%),
    linear-gradient(100deg,#e8e2d2 0%,#ebe6da 35%,rgba(235,235,235,0) 90%);
  -webkit-mask-image:linear-gradient(180deg,#000 80%,transparent 100%);
  mask-image:linear-gradient(180deg,#000 80%,transparent 100%)}
.hero-photo{left:362px;top:93px;width:400px;height:306px;
  background:
    radial-gradient(ellipse 90px 110px at 45% 32%,#9d9d9d 0%,#b5b5b5 45%,rgba(190,190,190,0) 100%),
    radial-gradient(ellipse 150px 80px at 48% 78%,#d9d9d9 0%,#cfcfcf 40%,rgba(210,210,210,0) 100%),
    radial-gradient(ellipse 70px 140px at 80% 45%,#e4e4e4 0%,rgba(228,228,228,0) 100%),
    radial-gradient(ellipse 50% 55% at 50% 45%,#bcbcbc 0%,#cdcdcd 55%,rgba(235,235,235,0) 100%);
  -webkit-mask-image:radial-gradient(ellipse 52% 60% at 50% 45%,#000 65%,transparent 100%);
  mask-image:radial-gradient(ellipse 52% 60% at 50% 45%,#000 65%,transparent 100%)}
.main-nav{left:724px;top:11px;display:flex;font:700 10.5px "Ubuntu",sans-serif;color:var(--muted)}
.main-nav a{color:inherit;text-decoration:none;padding:0 9px;border-left:1px solid #b8b8b8;line-height:14px}
.main-nav a:first-child{border-left:0}
.brand{left:857px;top:27px;width:117px;height:39px;background:#000;display:flex;align-items:center;gap:5px;padding-left:4px;color:#fff;font:400 6.5px "Arimo",Arial,sans-serif;letter-spacing:1px;white-space:nowrap;overflow:hidden}
.brand-dot{width:31px;height:31px;border-radius:50%;background:#fff;flex:none}

/* slider */
.slider-arrow{width:23px;height:23px;border-radius:50%;background:var(--arrow)}
.slide-photo{left:300px;top:427px;width:94px;height:111px;background:linear-gradient(160deg,#8a7a66,#b7a996 55%,#e6e0d6)}
.slide-title{left:439px;top:426px;font:700 19px "Gelasio",Georgia,serif;color:var(--ink)}
.slide-text{left:439px;top:458px;width:492px;font:400 10.6px/14.5px "Gelasio",Georgia,serif;color:var(--ink)}
.slider-dots{left:557px;top:550px;display:flex;gap:7px}
.slider-dots span{width:11px;height:11px;border-radius:50%;background:#9a9a9a;color:#fff;font:700 7px/11px "Arimo",sans-serif;text-align:center}
.slider-dots .is-active{background:#3a3a3a}

/* content columns */
.col-title{font:400 18px "Ubuntu",sans-serif;color:var(--accent);text-align:right}
.sub-title{font:400 12.5px "Ubuntu",sans-serif;color:var(--muted)}
.bullets{list-style:none;font-size:10px;color:var(--ink)}
.bullets li{height:19px;padding-left:13px;position:relative}
.bullets li::before{content:"";position:absolute;left:5px;top:3px;border-left:5px solid #8a8a8a;border-top:4px solid transparent;border-bottom:4px solid transparent}
.blurb{font-size:9.8px;line-height:11.5px;color:var(--text)}
.rule{height:1px;background:var(--rule)}
.thumb{display:block}
.measure-btn{left:495px;top:932px;width:115px;height:25px;border:1px solid #aaa;border-radius:3px;background:linear-gradient(#fafafa,#d8d8d8);box-shadow:0 1px 2px rgba(0,0,0,.2);font:400 10.5px/23px "Ubuntu",sans-serif;color:#222;text-align:center}

/* footer */
.site-footer{left:0;top:982px;width:1200px;height:203px;background:var(--footer-bg)}
.foot-col h4{font:400 13px "Arimo",sans-serif;color:var(--footer-head);margin-bottom:10px}
.foot-col a{display:block;font-size:10px;line-height:12px;color:var(--footer-link);text-decoration:none}
.copyright{left:0;top:1095px;width:1189px;text-align:center;font-size:10px;color:var(--footer-note)}
.share-btn{width:22px;height:22px;border-radius:50%;background:#8d8d8d}
</style>
</head>
<body>

<header>
  <div class="abs header-band"></div>
  <div class="abs header-photo" role="img" aria-label="Soft photograph of an ivory rose, pearls and wedding rings"></div>
  <div class="abs hero-photo" role="img" aria-label="Black and white portrait of a bride with veil and jewellery"></div>
  <nav class="abs main-nav">
    <a href="#">Home</a><a href="#">Build A Dress</a><a href="#">About Us</a><a href="#">Contacts</a>
  </nav>
  <div class="abs brand"><span class="brand-dot"></span>VELMARASTITCH</div>
</header>

<section class="slider">
  <svg class="abs slider-arrow" style="left:226px;top:471px" viewBox="0 0 23 23"><path d="M13.5 7 L9 11.5 L13.5 16" fill="none" stroke="#fff" stroke-width="2.2"/></svg>
  <svg class="abs slider-arrow" style="left:947px;top:471px" viewBox="0 0 23 23"><path d="M9.5 7 L14 11.5 L9.5 16" fill="none" stroke="#fff" stroke-width="2.2"/></svg>
  <div class="abs slide-photo" role="img" aria-label="Model wearing a modern fitted lace wedding gown"></div>
  <h2 class="abs slide-title">Modern</h2>
  <p class="abs slide-text">Lorem ipsum dolor sit amet, consectetur adipiscing elit. Nunc dapibus convallis justo vitae volutpat. Cras et sem sapien, nec semper felis. Proin id malesuada sem. Nullam ipsum dui, aliquet nec imperdiet sed, porttitor a enim.</p>
  <div class="abs slider-dots"><span>1</span><span>2</span><span class="is-active">3</span><span>4</span><span>5</span></div>
</section>

<section>
  <h3 class="abs col-title" style="left:235px;top:598px;width:228px">Create A Gown</h3>
  <h4 class="abs sub-title" style="left:235px;top:628px">Style</h4>
  <ul class="abs bullets" style="left:235px;top:663px">
    <li>Lorem ipsum dolor sit amet</li><li>Consectetur adipiscing elit</li><li>Etiam pharetra</li><li>Tellus sit amet congue</li><li>Vulputate, nisi erat iaculis</li>
  </ul>
  <div class="abs thumb" style="left:388px;top:655px;width:76px;height:114px;background:linear-gradient(135deg,#6b5236,#b69a6e 55%,#d9c9a8)" role="img" aria-label="Dressmaker's mannequin beside a chair"></div>
  <div class="abs rule" style="left:235px;top:787px;width:228px"></div>
  <h4 class="abs sub-title" style="left:235px;top:802px">Fabric</h4>
  <ul class="abs bullets" style="left:235px;top:838px">
    <li>Cras elit nisl, rhoncus nec</li><li>Iaculis ultricies, feugiat eget</li><li>Sapien.</li><li>Pellentesque ac felis tellus</li><li>Aenean sollicitudin</li><li>Arcu, vitae dignissim est</li>
  </ul>
  <div class="abs thumb" style="left:388px;top:830px;width:76px;height:114px;background:linear-gradient(150deg,#cfc6bb,#8e8379 50%,#e8e4de)" role="img" aria-label="Woman draped in flowing fabric"></div>
</section>

<section>
  <h3 class="abs col-title" style="left:493px;top:598px;width:244px">Measure Yourself</h3>
  <h4 class="abs sub-title" style="left:493px;top:628px">Lorem ipsum</h4>
  <p class="abs blurb" style="left:493px;top:651px;width:118px">Amet, consectetur adipiscing elitph, tellus sit amet adipiscing congue vulputate, nisi erat iaculis nibh.</p>
  <div class="abs thumb" style="left:623px;top:651px;width:114px;height:57px;background:linear-gradient(90deg,#7a7a7a,#c9c9c9 45%,#f2f2f2 70%,#dcdcdc)" role="img" aria-label="Sewing machine with spools of white thread"></div>
  <div class="abs rule" style="left:493px;top:724px;width:244px"></div>
  <h4 class="abs sub-title" style="left:493px;top:739px">Cras elit nisl</h4>
  <p class="abs blurb" style="left:493px;top:763px;width:110px">Rhoncus nec iaculis ultricies, feugiat eget sapien pellentesque ac felis tellus aenean sollicitudin.</p>
  <div class="abs thumb" style="left:623px;top:763px;width:114px;height:57px;background:linear-gradient(90deg,#3a2a26,#d9d3cc 45%,#5a2d2a 80%,#2b2222)" role="img" aria-label="Bride being fitted for her gown"></div>
  <div class="abs rule" style="left:493px;top:835px;width:244px"></div>
  <h4 class="abs sub-title" style="left:493px;top:850px">Duis placerat justo</h4>
  <p class="abs blurb" style="left:493px;top:874px;width:118px">Eu nunc interdum ultrices consectetur sit amet, posuere id magna a sollicitudin est.</p>
  <div class="abs thumb" style="left:623px;top:874px;width:114px;height:57px;background:linear-gradient(90deg,#5a2226,#b06a5e 40%,#e7e2de 75%,#f4f1ee)" role="img" aria-label="Seamstress measuring a dress"></div>
  <div class="abs measure-btn">Measure Yourself</div>
</section>

<section>
  <h3 class="abs col-title" style="left:767px;top:598px;width:198px">Agent Locator</h3>
  <h4 class="abs sub-title" style="left:767px;top:628px">Agent 1</h4>
  <p class="abs blurb" style="left:767px;top:651px;width:180px">Lorem ipsum dolor sit amet, consectetur adipiscing elit. Pellentesque ac felis tellus. Donec ut hendrerit enim.</p>
  <div class="abs rule" style="left:767px;top:701px;width:198px"></div>
  <h4 class="abs sub-title" style="left:767px;top:716px">Agent 2</h4>
  <p class="abs blurb" style="left:767px;top:740px;width:198px">Etiam pharetra, tellus sit amet congue vulputate, nisi erat iaculis nibh, vitae feugiat sapien ante eget mauris.</p>
  <div class="abs rule" style="left:767px;top:790px;width:198px"></div>
  <h4 class="abs sub-title" style="left:767px;top:805px">Agent 3</h4>
  <p class="abs blurb" style="left:767px;top:828px;width:190px">Cras elit nisl, rhoncus nec iaculis ultricies, feugiat eget sapien. Pellentesque ac felis tellus.</p>
  <div class="abs rule" style="left:767px;top:878px;width:198px"></div>
  <h4 class="abs sub-title" style="left:767px;top:893px">Agent 4</h4>
  <p class="abs blurb" style="left:767px;top:917px;width:198px">Aenean sollicitudin imperdiet arcu, vitae dignissim est posuere id. Duis placerat justo eu nunc interdum ultrices.</p>
</section>

<footer>
  <div class="abs site-footer"></div>
  <div class="abs foot-col" style="left:235px;top:1011px"><h4>Information</h4><a href="#">Home</a><a href="#">Agent Locator</a></div>
  <div class="abs foot-col" style="left:395px;top:1011px"><h4>Directions</h4><a href="#">Location</a><a href="#">Area Map</a><a href="#">Address</a><a href="#">Contact Us</a></div>
  <div class="abs foot-col" style="left:594px;top:1011px"><h4>Building A Gown</h4><a href="#">How To Measure</a><a href="#">How It Works</a><a href="#">Order Sample</a><a href="#">Support</a></div>
  <div class="abs foot-col" style="left:794px;top:1011px"><h4>Company</h4><a href="#">About Us</a><a href="#">Terms Of Use</a></div>
  <p class="abs copyright">Copyright © 2011 All Rights Reserved.</p>
  <span class="abs share-btn" style="left:564px;top:1119px"></span>
  <span class="abs share-btn" style="left:590px;top:1119px"></span>
  <span class="abs share-btn" style="left:617px;top:1119px"></span>
</footer>

</body>
</html>
```